Flyer for an pediatric sleep consultancy - to distribute to play and childcare centers etc.

I need a flyer that will attract the attention of parents with children between the age of babies to toddlers, who may be experiencing sleep issues. The flyer will be placed at places such as community centers, doctors room, play centers, kindergardens, etc.

My company is called "The Quiet Meadow Studio" and provides a sleep consultancy service. My service essentially provides a customized plan for parents to follow and general advice and guidance. It is not medical advice.

I like to the flyer to have an overall tone that is soft and peaceful with a clean and beautiful design, however can catch the attention of parents who may be struggling with their child's sleep issues and are sleep deprived. I would like photos with minimal text. The colour I use is a brownish rose. I will attach some of my designs to give you an idea. You can have a look at my homepage as well to get an idea about my esthetic direction and the colour. Although the colour of my page is a bit too brownish....

I will provide the text to appear in the flyer once I have a better idea of the layout that I prefer for the flyer. The text however wont be extensive, just some catchy points.

I want to direct people to my website which is www.quietmeadowstudio-example.com
I offer a first FREE evaluation call, to the parents, to get to know each other better, learn about their child's particular sleep problems and see if we are a good fit and can work together. I would like to have this information somehow on the flyer, so that the parents will contact me.
I also have a facebook page, which is: The Quiet Meadow Studio

I have a logo that I would like to appear on the flyer. I will attach the file once the uploader on art bazaar is fixed.

When I print the flyer - I like to print A5 SIZE ... please make sure the formatting is OK for this size.

Here are some text ideas. of course all of it would be too much, I guess. On the front of the flyer I would like to have some catchy phrase or something similar to get people interested and to want to know more. On the back there could be a bit more text and information. But I'm open too suggestions....
I'm not too sure about the wording yet. But here are some text that I might be use:

Is sleep an issue in your home?

Is your baby having trouble sleeping? ... are you?!
I can help!

Sleep, baby, sleep….

Teaching children how to sleep

The Quiet Meadow Studio is a pediatric sleep consultancy that specializes in helping parents with children who struggle to develop good and healthy sleep habits.
Disruptive sleep patterns or not enough sleep can affect the physical, mental and emotional development of your child.

Of course nobody plans to have a sleep problem, but habits can become easily ingrained and spiral quickly out of control and you can find yourself sleep deprived, desperate and not too sure what to do. You see all the other sleeping babies and wish there was someone who understood what you were going through?! Well, there is!

Contact me for a free 15 minute consultation.

This 15 minute „mini“ consultation is a chance to discuss your unique sleep challenges and sleep goals with me. I will provide you with an overview of how I will work with your family to achieve your wildest sleep dreams (goals).
Furthermore do I understand and believe that every child and their family is unique and there is no one size fits all!
I would love to have a chat with you and talk about how I can help make things easier for you and your family!

Do I need a sleep consultant for my child?
The answer is yes if:
- if your child will only fall asleep when nursing or bottle feeding
- if your child needs a dummy or other external aid, like being rocked, patted or taken for a care ride to fall asleep
- if your good night routine is a challenging and exhausting procedure instead of a relaxed and enjoyable moment for the whole family
- if sleep is a constant battle in your home which leaves you feeling frustrated and exhausted
- if your own lack of sleep is taking a toll on you and the whole family

What can I do for you?

I will:

- Guide you to set an age appropriate foundation for good sleep
- Create an individual sleep plan tailored especially to your child’s sleep needs and circumstances
- Help you to teach your childto go to sleep and get back to sleep independently during the night
- show you how to teach your child to take healthful, restorative naps
-Learn

Contact:

Marta Lindqvist
info@quietmeadowstudio-example.com
www.quietmeadowstudio-example.com
+34 612 380 574

Consultations in English, German or Spanish via Phone/VideoLink or home consultation

Reason: I have to go on a business trip and won't be able to choose a design until the deadline. During the trip I won't have time to give feedback and ask for changes. thank you

Target Market(s)

parents, sleep deprived mothers, young families, child care provider,

Industry/Entity Type

Baby Care

Contact Information for Business Card

Marta Lindqvist
pediatric sleep consultant
+34 612 380 574

```html
<!DOCTYPE html>
<html lang="en">
<head>
<meta charset="utf-8">
<title>The Quiet Meadow Studio – A5 Flyer</title>
<link rel="stylesheet" href="https://fonts.googleapis.com/css2?family=Cinzel:wght@700&family=Cormorant+Garamond:wght@500&family=Open+Sans:wght@400;600;700&family=Raleway:wght@300;500;600&display=swap">
<style>
  :root {
    --rose: #e4877b;
    --rose-soft: #f2c3bb;
    --sage: #8f9b92;
    --ink: #3a3a3a;
    --paper: #ffffff;
    --backdrop: #ece7e2;
    --photo-light: #f3efec;
    --photo-mid: #dcd5d0;
    --skin: #e9c2b0;
  }
  * { box-sizing: border-box; margin: 0; padding: 0; }
  html, body { width: 1200px; height: 900px; overflow: hidden; }
  body { background: var(--backdrop); font-family: "Open Sans", sans-serif; color: var(--ink); }
  .canvas { position: relative; width: 1200px; height: 900px; }

  .page { position: absolute; background: var(--paper); overflow: hidden; box-shadow: 0 2px 10px rgba(0,0,0,.12); }
  .page--front { left: 35px; top: 60px; width: 552px; height: 785px; }
  .page--back { left: 615px; top: 57px; width: 555px; height: 786px; }
  .abs { position: absolute; }

  /* brand */
  .brand { display: flex; flex-direction: column; align-items: center; gap: 8px; }
  .brand__mark { width: 46px; height: 46px; border: 1.5px solid var(--rose); border-radius: 50%; }
  .brand__name { font-family: "Raleway", sans-serif; font-weight: 300; color: var(--sage); font-size: 19px; letter-spacing: .2px; white-space: nowrap; }

  .photo { position: absolute; }

  /* front */
  .front__brand { left: 0; width: 100%; top: 44px; }
  .front__photo { left: 0; top: 125px; width: 552px; height: 300px;
    background: linear-gradient(180deg, var(--photo-light) 0%, #e9e4e0 45%, var(--photo-mid) 100%); }
  .front__bands { left: 0; top: 0; width: 552px; height: 785px; }
  .headline { left: 20px; width: 522px; top: 455px; text-align: center; color: var(--paper); }
  .headline__main { font-family: "Cinzel", serif; font-weight: 700; font-size: 26px; line-height: 35px; letter-spacing: .2px; white-space: nowrap; }
  .headline__sub { font-family: "Cormorant Garamond", serif; font-weight: 500; font-size: 22px; line-height: 24px; padding-right: 20px; }
  .headline__tag { font-family: "Raleway", sans-serif; font-weight: 600; font-size: 14px; line-height: 19px; margin-top: 4px; padding-right: 20px; }
  .front__circle { left: 447px; top: 494px; width: 106px; height: 106px; border-radius: 50%;
    border: 4px solid var(--paper); box-shadow: 0 0 0 2px var(--rose);
    background: radial-gradient(circle at 45% 45%, #f6e6df 0%, var(--skin) 60%, #d7c7c0 100%); }

  .section-title { display: flex; align-items: center; gap: 6px; left: 92px; width: 325px; top: 580px; line-height: 22px;
    font-family: "Raleway", sans-serif; font-weight: 500; font-size: 17px; color: var(--rose); white-space: nowrap; }
  .section-title::before, .section-title::after { content: ""; flex: 1; height: 1px; background: var(--rose); }
  .front__body { left: 35px; width: 482px; top: 604px; font-size: 10.6px; line-height: 14px; text-align: justify; }
  .front__body p + p { margin-top: 5px; }

  .contact-bar { left: 0; top: 715px; width: 552px; height: 37px; background: var(--rose); color: var(--paper);
    display: flex; align-items: center; justify-content: center; gap: 10px; font-weight: 600; font-size: 10.5px; white-space: nowrap; }
  .contact-bar__item { display: flex; align-items: center; gap: 4px; }
  .icon { width: 11px; height: 11px; fill: currentColor; flex: none; }
  .url-bar { left: 0; top: 752px; width: 552px; height: 33px; background: var(--sage); color: var(--paper);
    display: flex; align-items: center; justify-content: center; font-size: 12px; }

  /* back */
  .back__photo { left: 0; top: 0; width: 555px; height: 280px;
    background: linear-gradient(180deg, #d9d6d4 0%, #ebe8e6 55%, var(--paper) 100%); }
  .back__hand { left: 460px; top: 340px; width: 95px; height: 330px;
    background: linear-gradient(90deg, rgba(233,194,176,0) 0%, var(--skin) 55%, #e3b8a6 100%); }
  .back__title { left: 0; width: 555px; top: 228px; text-align: center; font-family: "Cinzel", serif; font-weight: 700;
    font-size: 14.5px; color: var(--rose); }
  .back__intro { left: 40px; width: 475px; top: 248px; font-size: 10.6px; line-height: 14.6px; text-align: justify; }
  .label { background: var(--rose); color: var(--paper); font-family: "Raleway", sans-serif; font-weight: 600;
    font-size: 14px; padding: 4px 12px; white-space: nowrap; }
  .label--need { left: 40px; top: 326px; width: 322px; }
  .label--do { left: 125px; top: 516px; width: 176px; }
  .lead { font-weight: 700; font-size: 11.5px; }
  .lead--yes { left: 45px; top: 357px; }
  .lead--will { left: 130px; top: 543px; }

  .checklist { list-style: none; font-size: 10.6px; line-height: 15px; }
  .checklist li { position: relative; padding-left: 21px; margin-bottom: 4px; }
  .checklist li::before { content: ""; position: absolute; left: 0; top: 2px; width: 11px; height: 11px; border: 1px solid var(--rose); }
  .checklist li::after { content: ""; position: absolute; left: 3px; top: 2px; width: 4px; height: 8px;
    border-right: 2px solid var(--rose); border-bottom: 2px solid var(--rose); transform: rotate(40deg); }
  .checklist--need { left: 45px; top: 375px; width: 395px; }
  .checklist--will { left: 130px; top: 562px; width: 285px; line-height: 14px; }
  .checklist--will li { margin-bottom: 2px; }

  .back__portrait { left: 22px; top: 518px; width: 103px; height: 178px;
    background: linear-gradient(180deg, #efe3d6 0%, #c9b9ad 50%, #4a4a52 100%); }
  .back__bands { left: 0; top: 0; width: 555px; height: 786px; }
  .back__brand { left: 20px; top: 712px; width: 170px; gap: 6px; }
  .back__brand .brand__mark { width: 30px; height: 30px; border-color: var(--paper); }
  .back__brand .brand__name { color: var(--paper); font-size: 13px; }
  .badge { left: 228px; top: 676px; width: 94px; height: 94px; border-radius: 50%; background: var(--rose);
    border: 4px solid var(--paper); box-shadow: 0 0 0 1px var(--rose); color: var(--paper);
    display: flex; align-items: center; justify-content: center; text-align: center;
    font-size: 7.4px; font-weight: 600; line-height: 9.2px; padding: 8px; }
  .back__contact { right: 16px; top: 703px; text-align: right; color: var(--paper); line-height: 15px; }
  .back__contact-label { font-family: "Raleway", sans-serif; font-size: 13px; }
  .back__contact-name { font-weight: 700; font-size: 13px; letter-spacing: .3px; }
  .back__contact-phone { font-weight: 700; font-size: 14px; line-height: 17px; display: flex; justify-content: flex-end; align-items: center; gap: 6px; }
  .back__contact-line { font-size: 10.5px; line-height: 13.5px; display: flex; justify-content: flex-end; align-items: center; gap: 5px; }
  .back__contact .icon { width: 10px; height: 10px; }
  .back__contact-phone .icon { width: 13px; height: 13px; }
</style>
</head>
<body>
<main class="canvas">

  <!-- Front side -->
  <section class="page page--front">
    <div class="photo front__photo" role="img" aria-label="Photo of a newborn baby sleeping in a white cot"></div>

    <svg class="abs front__bands" viewBox="0 0 552 785" aria-hidden="true">
      <path d="M0,0 H552 V120 Q276,150 0,120 Z" fill="#ffffff"/>
      <path d="M0,375 Q276,445 552,365 V565 H0 Z" fill="var(--sage)"/>
      <path d="M0,390 Q276,462 552,380 V565 H0 Z" fill="#ffffff"/>
      <path d="M0,396 Q276,470 552,386 V565 H0 Z" fill="var(--rose)"/>
      <rect x="0" y="565" width="552" height="150" fill="#ffffff"/>
    </svg>

    <div class="abs brand front__brand">
      <span class="brand__mark"></span>
      <span class="brand__name">The Quiet Meadow Studio</span>
    </div>

    <div class="abs headline">
      <h1 class="headline__main">IS SLEEP AN ISSUE IN YOUR HOME?</h1>
      <p class="headline__sub">Is your baby having trouble sleeping?<br>... are you?! I can help!</p>
      <p class="headline__tag">Sleep, baby, sleep….</p>
    </div>

    <div class="abs front__circle" role="img" aria-label="Round photo of a toddler sleeping peacefully"></div>

    <h2 class="abs section-title">Teaching Children How To Sleep</h2>

    <div class="abs front__body">
      <p>The Quiet Meadow Studio is a pediatric sleep consultancy that specializes in helping parents with children who struggle to develop good and healthy sleep habits. Disruptive sleep patterns or not enough sleep can affect the physical, mental and emotional development of your child.</p>
      <p>Of course nobody plans to have a sleep problem, but habits can become easily ingrained and spiral quickly out of control and you can find yourself sleep deprived, desperate and not too sure what to do. You see all the other sleeping babies and wish there was someone who understood what you were going through?! Well, there is!</p>
    </div>

    <div class="abs contact-bar">
      <span>Contact:</span>
      <span class="contact-bar__item">
        <svg class="icon" viewBox="0 0 12 12"><circle cx="6" cy="3.5" r="2.6"/><path d="M1,12 Q1,6.8 6,6.8 Q11,6.8 11,12 Z"/></svg>
        Marta Lindqvist
      </span>
      <span class="contact-bar__item">
        <svg class="icon" viewBox="0 0 12 12"><path d="M2.5,0.8 L4.5,0.5 L5.3,3.4 L4,4.4 Q5,6.9 7.6,8 L8.6,6.7 L11.5,7.5 L11.2,9.5 Q10.5,11.5 8,11 Q2,9 1,3.5 Q0.8,1.5 2.5,0.8 Z"/></svg>
        +34 612 380 574
      </span>
      <span class="contact-bar__item">
        <svg class="icon" viewBox="0 0 12 12"><path d="M0.5,2.5 H11.5 V9.5 H0.5 Z M1.5,3.4 V8.6 H10.5 V3.4 L6,6.6 Z" fill-rule="evenodd"/></svg>
        info@quietmeadowstudio-example.com
      </span>
    </div>
    <div class="abs url-bar">www.quietmeadowstudio-example.com</div>
  </section>

  <!-- Back side -->
  <section class="page page--back">
    <div class="photo back__photo" role="img" aria-label="Photo of a toddler peeking over the edge of a white blanket"></div>
    <div class="photo back__hand" role="img" aria-label="Photo of a baby's hand holding an adult's finger"></div>

    <h2 class="abs back__title">CONTACT ME FOR A FREE 15 MINUTE CONSULTATION.</h2>
    <p class="abs back__intro">This 15 minute „mini“ consultation is a chance to discuss your unique sleep challenges and sleep goals with me. I will provide you with an overview of how I will work with your family to achieve your wildest sleep dreams (goals). Furthermore do I understand and believe that every child and their family is unique and there is no one size fits all! I would love to have a chat with you and talk about how I can help make things easier for you and your family!</p>

    <h3 class="abs label label--need">Do I need a sleep consultant for my child?</h3>
    <p class="abs lead lead--yes">The answer is yes if:</p>
    <ul class="abs checklist checklist--need">
      <li>if your child will only fall asleep when nursing or bottle feeding</li>
      <li>if your child needs a dummy or other external aid, like being rocked, patted or taken for a care ride to fall asleep</li>
      <li>if your good night routine is a challenging and exhausting procedure instead of a relaxed and enjoyable moment for the whole family</li>
      <li>if sleep is a constant battle in your home which leaves you feeling frustrated and exhausted</li>
      <li>if your own lack of sleep is taking a toll on you and the whole family</li>
    </ul>

    <div class="photo back__portrait" role="img" aria-label="Photo of the consultant holding a toddler"></div>

    <h3 class="abs label label--do">What can I do for you?</h3>
    <p class="abs lead lead--will">I will :</p>
    <ul class="abs checklist checklist--will">
      <li>Guide you to set an age appropriate foundation for good sleep</li>
      <li>Create an individual sleep plan tailored especially to your child’s sleep needs and circumstances</li>
      <li>Help you to teach your childto go to sleep and get back to sleep independently during the night</li>
      <li>show you how to teach your child to take healthful, restorative naps</li>
      <li>Learn</li>
    </ul>

    <svg class="abs back__bands" viewBox="0 0 555 786" aria-hidden="true">
      <path d="M0,680 Q250,752 555,636 V786 H0 Z" fill="var(--sage)"/>
      <path d="M0,689 Q250,763 555,646 V786 H0 Z" fill="#ffffff"/>
      <path d="M0,695 Q250,770 555,652 V786 H0 Z" fill="var(--rose)"/>
    </svg>

    <div class="abs brand back__brand">
      <span class="brand__mark"></span>
      <span class="brand__name">The Quiet Meadow Studio</span>
    </div>

    <div class="abs badge">Consultations in English, German or Spanish via Phone/VideoLink or home consultation</div>

    <div class="abs back__contact">
      <p class="back__contact-label">Contact:</p>
      <p class="back__contact-name">MARTA LINDQVIST</p>
      <p class="back__contact-phone">
        <svg class="icon" viewBox="0 0 12 12"><path d="M2.5,0.8 L4.5,0.5 L5.3,3.4 L4,4.4 Q5,6.9 7.6,8 L8.6,6.7 L11.5,7.5 L11.2,9.5 Q10.5,11.5 8,11 Q2,9 1,3.5 Q0.8,1.5 2.5,0.8 Z"/></svg>
        +34 612 380 574
      </p>
      <p class="back__contact-line">
        <svg class="icon" viewBox="0 0 12 12"><path d="M0.5,2.5 H11.5 V9.5 H0.5 Z M1.5,3.4 V8.6 H10.5 V3.4 L6,6.6 Z" fill-rule="evenodd"/></svg>
        info@quietmeadowstudio-example.com
      </p>
      <p class="back__contact-line">
        <svg class="icon" viewBox="0 0 12 12"><circle cx="6" cy="6" r="5.3" fill="none" stroke="currentColor" stroke-width="1.2"/><path d="M0.8,6 H11.2 M6,0.7 Q2.8,6 6,11.3 M6,0.7 Q9.2,6 6,11.3" fill="none" stroke="currentColor" stroke-width="1"/></svg>
        www.quietmeadowstudio-example.com
      </p>
    </div>
  </section>

</main>
</body>
</html>
```